Business Card Design, including supply of raw art files plus a vector diagram of the zelvon logo and

We need the business card design for a company that is launching a new exciting product. The brief requires the submission of the following once the final design is chosen:

- business card layout including raw files
- a composite vector image file of the zelvon logo and tag line
- a standalone vector image file of the zelvon logo

The product will be launched as a customer engagement app.

It has 4 core modules which enables a person to do multiple things - book tours and activities, order takeaways, search for local deals and offers. A universal currency is at the heart of this product. When you use the app, you earn cashback rewards when shopping or buying at any of the merchant partners across the modules as . These rewards can then be used as full or part payment when buying goods or services at these merchant partners.

The business card must help us build the brand, communicate the benefit of the brand's key focus - the ability to earn and burn this universal cashback ccurrency - across the 4 modules - booking of tours and activities, ordering, searching for local deals and payment.

We would like the design to use the brand's blue colour the hex colour is: 00
Dark grey : 646464
Darker blue shadow: 058bdd
Main Blue: 0084ff

We need to translate this into a CMYK print or spot colour print.

Both print options to be supplied as separate files.

An example of the base concept we have in mind is attached for your reference.

The font used by the brand is Proxima Nova.

Note: the duration has been set as 2 days.

Industry/Entity Type

Business

Contact Information for Business Card

Carla Mendoza
Marketing
W: www.zelvon.example
M: + 61 400555123
T: +61 2 5550 1473
A: Suite 7, Level 2, 14-18 Harwick Street, Sydney, NSW, 2000, Australia

Font styles to use
Sans Serif

Requirements
Must have
• zelVon logo and tagline
• address details
• zelVon icons as supplied
Nice to have
• would like to have the option of a spot varnish layer over the logo and icons at the back of the card

```html
<!DOCTYPE html>
<html lang="en">
<head>
<meta charset="utf-8">
<title>zelVon business card</title>
<link rel="stylesheet" href="https://fonts.googleapis.com/css2?family=Roboto:wght@300;400&family=Roboto+Condensed:wght@400&display=swap">
<style>
  :root {
    --backdrop: #3b3e42;
    --brand-blue: #0a8fd6;
    --brand-blue-deep: #0478c0;
    --accent-blue: #1a7fc4;
    --dark-grey: #3f4246;
    --text-grey: #555a5f;
    --name-grey: #3e4247;
    --card-white: #f4f4f4;
    --white: #ffffff;
  }
  * { margin: 0; padding: 0; box-sizing: border-box; }
  html, body { width: 1200px; height: 576px; overflow: hidden; }
  body {
    background: var(--backdrop);
    font-family: "Roboto", Arial, sans-serif;
    position: relative;
  }
  .card {
    position: absolute;
    top: 138px;
    width: 485px;
    height: 292px;
    overflow: hidden;
  }
  /* Back of card */
  .card--back {
    left: 81px;
    background: linear-gradient(160deg, var(--brand-blue) 0%, var(--brand-blue-deep) 100%);
    color: var(--white);
  }
  .brand-mark {
    position: absolute;
    border-radius: 50%;
  }
  .card--back .brand-mark {
    left: 112px; top: 62px; width: 76px; height: 76px;
    background: var(--white);
  }
  .brand-lockup {
    position: absolute;
    left: 202px; top: 72px;
    display: flex;
    flex-direction: column;
    align-items: flex-end;
  }
  .brand-name {
    font-weight: 300;
    line-height: 1;
    white-space: nowrap;
  }
  .card--back .brand-name {
    font-size: 48px;
    color: var(--white);
  }
  .tagline {
    margin-top: -4px;
    font-size: 15px;
    font-weight: 300;
    line-height: 1;
    white-space: nowrap;
  }
  .modules {
    position: absolute;
    left: 0; top: 218px;
    width: 100%;
    list-style: none;
  }
  .module {
    position: absolute;
    width: 90px;
    margin-left: -45px;
    text-align: center;
    font-family: "Roboto Condensed", Arial, sans-serif;
    font-size: 10px;
    line-height: 1;
    white-space: nowrap;
  }
  .module svg { display: block; margin: 0 auto 7px; }
  .module--rewards { left: 131px; }
  .module--tours { left: 218px; }
  .module--ordering { left: 298px; }
  .module--offers { left: 368px; }

  /* Front of card */
  .card--front {
    left: 602px;
    background: var(--card-white);
  }
  .card--front .brand-mark {
    left: 219px; top: 32px; width: 52px; height: 52px;
    background: var(--accent-blue);
  }
  .card--front .brand-name {
    position: absolute;
    left: 284px; top: 37px;
    font-size: 42px;
    color: var(--name-grey);
  }
  .contact-list {
    position: absolute;
    left: 233px; top: 144px;
    list-style: none;
    font-size: 13px;
    color: var(--text-grey);
    line-height: 16px;
  }
  .contact-item { position: relative; padding-left: 17px; }
  .contact-item svg { position: absolute; left: 0; top: 3px; }
  .person-name {
    position: absolute;
    left: 22px; top: 216px;
    font-size: 16px;
    font-weight: 400;
    color: var(--accent-blue);
  }
  .person-role {
    position: absolute;
    left: 22px; top: 240px;
    font-size: 12px;
    color: var(--text-grey);
  }
  .footer-band { position: absolute; left: 0; top: 256px; }
  .website {
    position: absolute;
    left: 233px; top: 268px;
    padding-left: 17px;
    font-size: 13px;
    font-weight: 300;
    color: var(--white);
  }
  .website svg { position: absolute; left: 0; top: 2px; }
</style>
</head>
<body>

<section class="card card--back" aria-label="Card back">
  <span class="brand-mark"></span>
  <div class="brand-lockup">
    <span class="brand-name">zelVon</span>
    <span class="tagline">rewards made simple</span>
  </div>

  <ul class="modules">
    <li class="module module--rewards">
      <svg width="30" height="28" viewBox="0 0 30 28">
        <rect x="4" y="3" width="22" height="22" rx="2" fill="#fff"/>
        <circle cx="15" cy="14" r="7" fill="var(--brand-blue)"/>
        <text x="15" y="18.5" text-anchor="middle" font-size="12" font-family="Roboto, sans-serif" fill="#fff">$</text>
      </svg>
      CashBack Rewards
    </li>
    <li class="module module--tours">
      <svg width="34" height="28" viewBox="0 0 34 28">
        <path d="M2 7h8l2-4h10l2 4h8v19H2z" fill="#fff"/>
        <circle cx="17" cy="16" r="7" fill="var(--brand-blue)"/>
        <circle cx="17" cy="16" r="4.5" fill="#fff"/>
      </svg>
      Tours &amp; Activities
    </li>
    <li class="module module--ordering">
      <svg width="30" height="28" viewBox="0 0 30 28" stroke="#fff" stroke-width="2" fill="none" stroke-linecap="round">
        <path d="M5 2v6a3 3 0 0 0 6 0V2M8 2v6M8 11l17 15"/>
        <path d="M5 26l13-13"/>
        <ellipse cx="21" cy="8" rx="3.5" ry="5.5" transform="rotate(45 21 8)" fill="#fff"/>
      </svg>
      Mobile Ordering
    </li>
    <li class="module module--offers">
      <svg width="30" height="28" viewBox="0 0 30 28">
        <path d="M16 2h12v12L14 27 2 15z" fill="#fff"/>
        <circle cx="22.5" cy="7.5" r="2.2" fill="var(--brand-blue)"/>
      </svg>
      Local Offers
    </li>
  </ul>
</section>

<section class="card card--front" aria-label="Card front">
  <span class="brand-mark"></span>
  <span class="brand-name">zelVon</span>

  <ul class="contact-list">
    <li class="contact-item">
      <svg width="9" height="11" viewBox="0 0 9 11"><rect x="1" y="0" width="7" height="11" rx="1" fill="var(--accent-blue)"/><rect x="2.5" y="1.5" width="4" height="6.5" fill="var(--card-white)"/></svg>
      + 61 400555123
    </li>
    <li class="contact-item">
      <svg width="12" height="10" viewBox="0 0 12 10"><path d="M0 3Q6-1 12 3v2H9V3.5H3V5H0z M2 6h8l1 4H1z" fill="var(--accent-blue)"/></svg>
      +61 2 5550 1473
    </li>
    <li class="contact-item">
      <svg width="10" height="13" viewBox="0 0 10 13"><path d="M5 0a5 5 0 0 1 5 5c0 3-5 8-5 8S0 8 0 5a5 5 0 0 1 5-5z" fill="var(--accent-blue)"/><circle cx="5" cy="5" r="1.8" fill="var(--card-white)"/></svg>
      Suite 7, Level 2, 14-18 Harwick Street,<br>Sydney NSW 2000, Australia
    </li>
  </ul>

  <h1 class="person-name">Carla Mendoza</h1>
  <p class="person-role">Marketing</p>

  <svg class="footer-band" width="485" height="36" viewBox="0 0 485 36" aria-hidden="true">
    <polygon points="0,18 190,18 184,36 0,36" fill="var(--dark-grey)"/>
    <polygon points="198,0 485,0 485,36 178,36" fill="var(--accent-blue)"/>
  </svg>
  <span class="website">
    <svg width="11" height="11" viewBox="0 0 11 11" fill="none" stroke="#fff" stroke-width="1"><circle cx="5.5" cy="5.5" r="4.8"/><ellipse cx="5.5" cy="5.5" rx="2" ry="4.8"/><path d="M0.7 5.5h9.6"/></svg>
    www.zelvon.example
  </span>
</section>

</body>
</html>
```